Marlow Creek sign

24"x36" sign for new home construction job site. Located in affluent in-town neighborhood in Midwest. Traditional american style homes. 2nd generation construction company. Sign needs to convey strength and elegance but not overly elaborate. Competition most has signs consisting of text.

Sign text reads:
Marlow Creek Builders
Custom Luxury for Over 20 years
248-555-0137

Target Market(s)

Upper middle income home buyers

Industry/Entity Type

Construction

Font styles to use
Serif
Decorative

Requirements
Must have
• Logo image no more than 2 colors
Nice to have
• Should be visible and legible from distance of 30'
Should not have
• Not just image of house as logo

```html
<!DOCTYPE html>
<html lang="en">
<head>
<meta charset="utf-8">
<title>Marlow Creek Builders – Job Site Sign</title>
<link rel="stylesheet" href="https://fonts.googleapis.com/css2?family=Graduate&family=Oswald:wght@700&display=swap">
<style>
  :root {
    --frame-red: #b0141b;
    --panel-red: #a8161d;
    --panel-blue: #0b5391;
    --sign-white: #ffffff;
    --shadow-ink: #1b1b1b;
    --swoosh-light: #f2f2f2;
    --swoosh-dark: #8a8a8a;
  }
  html, body {
    margin: 0;
    padding: 0;
    width: 1200px;
    height: 984px;
    overflow: hidden;
    background: var(--sign-white);
  }
  .sign {
    display: block;
    width: 1200px;
    height: 984px;
  }
  .frame-outer { fill: var(--frame-red); }
  .frame-gap { fill: var(--sign-white); }
  .panel-blue { fill: var(--panel-blue); }
  .panel-red { fill: var(--panel-red); }
  .phone-divider { stroke: var(--sign-white); stroke-width: 3; }
  .swoosh { fill: none; stroke: url(#swooshShade); stroke-width: 7; }
  .star { fill: var(--sign-white); }
  .headline,
  .tagline {
    font-family: "Graduate", "Georgia", serif;
    fill: var(--sign-white);
    text-anchor: middle;
    filter: drop-shadow(3px 4px 0 var(--shadow-ink));
  }
  .headline-name { font-size: 104px; }
  .headline-trade { font-size: 104px; }
  .tagline-lead { font-size: 70px; }
  .tagline-years { font-size: 104px; }
  .phone {
    font-family: "Oswald", "Arial Narrow", sans-serif;
    font-weight: 700;
    font-size: 96px;
    fill: var(--sign-white);
    text-anchor: middle;
  }
</style>
</head>
<body>
<svg class="sign" viewBox="0 0 1200 984" xmlns="http://www.w3.org/2000/svg" aria-label="Marlow Creek Builders job site sign">
  <defs>
    <linearGradient id="swooshShade" x1="0" y1="0" x2="1" y2="0">
      <stop offset="0" stop-color="var(--swoosh-dark)"/>
      <stop offset="0.5" stop-color="var(--swoosh-light)"/>
      <stop offset="1" stop-color="var(--swoosh-dark)"/>
    </linearGradient>
    <polygon id="starShape" points="0,-1 0.2245,-0.309 0.951,-0.309 0.363,0.118 0.588,0.809 0,0.382 -0.588,0.809 -0.363,0.118 -0.951,-0.309 -0.2245,-0.309"/>
  </defs>

  <!-- frame -->
  <rect class="frame-outer" x="116" y="150" width="983" height="657"/>
  <rect class="frame-gap" x="128" y="162" width="959" height="633"/>

  <!-- panels -->
  <rect class="panel-blue" x="138" y="172" width="939" height="613"/>
  <path class="panel-red" d="M138,172 H1077 V369 Q607.5,513 138,369 Z"/>
  <path class="swoosh" d="M138,375 Q607.5,519 1077,375"/>
  <line class="phone-divider" x1="138" y1="672" x2="1077" y2="672"/>

  <!-- stars -->
  <g class="stars">
    <use class="star" href="#starShape" transform="translate(503 414) scale(12)"/>
    <use class="star" href="#starShape" transform="translate(546 414) scale(12)"/>
    <use class="star" href="#starShape" transform="translate(592 410) scale(20)"/>
    <use class="star" href="#starShape" transform="translate(638 414) scale(12)"/>
    <use class="star" href="#starShape" transform="translate(681 414) scale(12)"/>
  </g>

  <!-- company name -->
  <text class="headline headline-name" x="607" y="276" textLength="880" lengthAdjust="spacingAndGlyphs">MARLOW CREEK</text>
  <text class="headline headline-trade" x="611" y="373" textLength="528" lengthAdjust="spacingAndGlyphs">BUILDERS</text>

  <!-- tagline -->
  <text class="tagline tagline-lead" x="611" y="547" textLength="696" lengthAdjust="spacingAndGlyphs">CUSTOM LUXURY FOR</text>
  <text class="tagline tagline-years" x="607" y="648" textLength="810" lengthAdjust="spacingAndGlyphs">OVER 20 YEARS</text>

  <!-- phone -->
  <text class="phone" x="592" y="769" textLength="640" lengthAdjust="spacingAndGlyphs">248-555-0137</text>
</svg>
</body>
</html>
```